I need a logo that demonstrates multiple of the same with one of a distinguishing feature. I would like something that can be recognisable in silhouette format. The business designs Management systems bespoke the to the company helping them pre-qualify for work.
Something that can demonstrate a distinction between a collective group non of which are the same in shape or size, with the largest of these not the distinguished object (or something to that effect).
This is a new business no logo or artwork exists.
Target Market(s)
Small to Medium Size enterprises in the city and rural areas. Looking to make the step up.
Industry/Entity Type
Manufacture
Contact Information for Business Card
room for, Name, Email, phone number
Font styles to use
Requirements
Must have
- would like the silhouette to be recognisable
Nice to have
- would like it to incorporate the name Quarrywell Advisory Systems.
- Would like the same logo to be on both business cards and on corporate shirts
Should not have
- anything that may exclude rural trade or manufacturing.
- I don't want to appear as corporate, just professional

```html
<!DOCTYPE html>
<html lang="en">
<head>
<meta charset="utf-8">
<title>Quarrywell Advisory Systems — Business Cards</title>
<link rel="stylesheet" href="https://fonts.googleapis.com/css2?family=Open+Sans:wght@400;700&display=swap">
<style>
  :root {
    --backdrop: #4d433e;
    --card: #141414;
    --card-edge: #0a0a0a;
    --brand-blue: #1e5fc4;
    --accent-red: #e0262a;
    --silver: #8d8d8d;
    --ink: #f2f2f2;
    --rule: #6b6b6b;
  }
  * { box-sizing: border-box; margin: 0; padding: 0; }
  html, body {
    width: 1200px; height: 860px; overflow: hidden;
    background: var(--backdrop);
    font-family: "Open Sans", Arial, sans-serif;
  }
  .canvas { position: relative; width: 1200px; height: 860px; }

  .card {
    position: absolute;
    width: 560px; height: 320px;
    background: var(--card);
    border-radius: 4px;
    box-shadow: 0 14px 30px rgba(0,0,0,.45);
  }
  .card--back { left: 50px; top: 80px; }
  .card--front { left: 590px; top: 460px; }

  /* back side: single-colour wordmark */
  .back-mark {
    position: absolute; left: 0; right: 0; top: 110px;
    text-align: center;
    color: var(--silver);
    font-weight: 700; font-size: 30px; letter-spacing: .5px;
    line-height: 1.15;
  }
  .back-mark .rule {
    display: block; width: 250px; height: 1px;
    margin: 14px auto 0; background: var(--silver);
  }

  /* front side */
  .front-mark {
    position: absolute; right: 34px; top: 30px;
    display: flex; align-items: center; gap: 10px;
    color: var(--brand-blue);
    font-weight: 700; font-size: 22px;
  }
  .front-mark .dot { width: 12px; height: 12px; background: var(--accent-red); }
  .front-mark-rule {
    position: absolute; right: 34px; top: 70px;
    width: 300px; height: 1px; background: var(--rule);
  }

  .holder {
    position: absolute; left: 30px; top: 120px; width: 220px;
    text-align: right; color: var(--ink);
    font-size: 15px; line-height: 1.45;
  }
  .holder .name {
    color: var(--brand-blue); font-weight: 700; font-size: 24px;
    line-height: 1.2; margin-bottom: 4px;
  }

  .divider {
    position: absolute; left: 270px; top: 130px;
    width: 1px; height: 140px;
    background: linear-gradient(to bottom, transparent, #9a9a9a, transparent);
  }

  .contacts {
    position: absolute; left: 288px; top: 122px;
    list-style: none; color: var(--ink);
    font-size: 16px; line-height: 30px;
  }
  .contacts li { display: flex; align-items: center; gap: 10px; }
  .contacts svg { width: 14px; height: 14px; fill: var(--brand-blue); flex: none; }
</style>
</head>
<body>
<main class="canvas">

  <section class="card card--back" aria-label="Card back">
    <div class="back-mark">Quarrywell Advisory Systems<span class="rule"></span></div>
  </section>

  <section class="card card--front" aria-label="Card front">
    <div class="front-mark"><span class="dot"></span>Quarrywell Advisory Systems</div>
    <div class="front-mark-rule"></div>

    <div class="holder">
      <p class="name">Martin Hale</p>
      <p>Managing Member</p>
      <p>2207 Foundry Lane,</p>
      <p>Fairbrook, CA 95012</p>
    </div>

    <div class="divider"></div>

    <ul class="contacts">
      <li><svg viewBox="0 0 24 24"><path d="M6.6 10.8a15 15 0 0 0 6.6 6.6l2.2-2.2a1 1 0 0 1 1-.25 11.4 11.4 0 0 0 3.6.57 1 1 0 0 1 1 1V20a1 1 0 0 1-1 1A17 17 0 0 1 3 4a1 1 0 0 1 1-1h3.5a1 1 0 0 1 1 1c0 1.25.2 2.45.57 3.57a1 1 0 0 1-.25 1z"/></svg>(555) 204-7316</li>
      <li><svg viewBox="0 0 24 24"><path d="M7 2h8l3 3v5H7zM4 11h16a2 2 0 0 1 2 2v7H2v-7a2 2 0 0 1 2-2zm3 5v2h10v-2z"/></svg>(555) 204-7317</li>
      <li><svg viewBox="0 0 24 24"><path d="M7 1h10a2 2 0 0 1 2 2v18a2 2 0 0 1-2 2H7a2 2 0 0 1-2-2V3a2 2 0 0 1 2-2zm0 3v14h10V4zm5 15.5a1 1 0 1 0 0 2 1 1 0 0 0 0-2z"/></svg>(555) 318-4492</li>
      <li><svg viewBox="0 0 24 24"><path d="M2 5h20v14H2zm2 2v.5l8 5 8-5V7l-8 5z"/></svg>martin@yourweb.com</li>
      <li><svg viewBox="0 0 24 24"><path d="M12 2a10 10 0 1 0 0 20 10 10 0 0 0 0-20zm-1 2.1V8H8.3A8 8 0 0 1 11 4.1zm2 0A8 8 0 0 1 15.7 8H13zM6.1 10H11v4H6.1a8 8 0 0 1 0-4zm6.9 0h4.9a8 8 0 0 1 0 4H13zm-4.7 6H11v3.9A8 8 0 0 1 8.3 16zm4.7 0h2.7A8 8 0 0 1 13 19.9z"/></svg>www.yourweb.com</li>
    </ul>
  </section>

</main>
</body>
</html>
```